Re-design of website

I have an existing website that I would like to improve. The functionality will remain the same but the overall look will need to be changed. I have some ideas of what i would like included and am also in need of someone else to input their own creative ideas. I am on a tight deadline to get these improvements made as I have many people being directed to the site via our advertising campaigns that are in full swing late next week. Thanks
Target Market(s)
The website provides a virtual space for families to learn more about our learning program which we operate out of Dubai and will soon spread to the other Emirates. The families are generally between 25-50 year old parents with children up to the age of 6. They are local Emirati's as well as expats.
Look and feel

```html
<!DOCTYPE html>
<html lang="en">
<head>
<meta charset="utf-8">
<title>Bright Sprouts – The Program</title>
<link rel="stylesheet" href="https://fonts.googleapis.com/css2?family=Merriweather:ital,wght@0,400;0,700;1,400&family=Source+Sans+3:wght@400;600;700&display=swap">
<style>
  :root {
    --navy: #0b3347;
    --white: #ffffff;
    --ink: #4a4a4a;
    --ink-dark: #333b40;
    --heading: #0b3347;
    --pink: #f2466b;
    --blue: #3aa8f0;
    --photo-warm: #8a5a3c;
    --photo-light: #d9c2a8;
  }
  * { box-sizing: border-box; margin: 0; padding: 0; }
  html, body {
    width: 1086px; height: 1200px; overflow: hidden;
    background: var(--navy);
    font-family: "Source Sans 3", "Source Sans Pro", sans-serif;
  }
  .page { position: relative; width: 1086px; height: 1200px; }

  .brand {
    position: absolute; left: 92px; top: 0; width: 196px; height: 254px;
    background: var(--white);
    display: flex; flex-direction: column; align-items: center; justify-content: center; gap: 14px;
  }
  .brand-mark { width: 22px; height: 22px; background: var(--navy); }
  .brand-name {
    font-family: "Merriweather", serif; font-weight: 700; font-size: 21px;
    color: var(--navy); text-align: center; line-height: 1.2;
  }

  .hero {
    position: absolute; left: 298px; top: 0; width: 698px; height: 254px;
    background: linear-gradient(100deg, #5a3526 0%, var(--photo-warm) 35%, var(--photo-light) 70%, #b9c3cc 100%);
  }

  .main-nav {
    position: absolute; left: 297px; top: 260px; width: 699px;
    display: flex; justify-content: space-between;
    font-size: 12.5px; font-weight: 600; text-transform: uppercase; letter-spacing: 0.1px;
  }
  .main-nav a { color: var(--white); text-decoration: none; }
  .main-nav a.is-current { color: var(--pink); }

  .cta {
    position: absolute; left: 92px; width: 196px;
    font-family: "Merriweather", serif; font-style: italic; color: var(--white);
    text-align: center; font-size: 17px; line-height: 24px;
  }
  .cta-register { top: 296px; height: 68px; background: var(--blue); padding-top: 10px; }
  .cta-contact { top: 372px; height: 104px; background: var(--pink); padding-top: 11px; }
  .social { display: flex; justify-content: center; gap: 11px; margin-top: 7px; }
  .social span { width: 24px; height: 24px; background: var(--white); display: block; }

  .content {
    position: absolute; left: 298px; top: 296px; width: 698px; height: 864px;
    background: var(--white);
  }
  .content-body {
    position: absolute; left: 32px; top: 25px; width: 462px;
    color: var(--ink); font-size: 14.5px; line-height: 19.2px;
  }
  .content-body h1 {
    font-family: "Merriweather", serif; font-weight: 700; font-size: 19.5px;
    color: var(--heading); margin-bottom: 18px; line-height: 28px;
  }
  .content-body p { margin-bottom: 19px; }
  .content-body strong { color: var(--ink-dark); font-weight: 700; }
  .benefits { list-style: none; margin-bottom: 45px; }
  .benefits li { position: relative; padding-left: 18px; }
  .benefits li::before {
    content: ""; position: absolute; left: 0; top: 6px;
    width: 7px; height: 7px; background: var(--pink);
  }
  .content-body h2 {
    font-family: "Merriweather", serif; font-weight: 700; font-size: 16.5px;
    color: var(--blue); margin-bottom: 19px; line-height: 24px;
  }
  .terms { margin-bottom: 19px; }
  .terms b { display: inline-block; width: 66px; color: var(--ink-dark); }
  .pricing { margin-bottom: 38px !important; }

  .side-photo { position: absolute; left: 510px; width: 155px; }
  .side-photo-abacus { top: 33px; height: 126px; background: linear-gradient(135deg, #c9b59a, #e8e2da 60%, #a47c5c); }
  .side-photo-play { top: 164px; height: 168px; background: linear-gradient(160deg, #e58a2e, #c7b3a0 45%, #2f55a8 100%); }

  .footer-note {
    position: absolute; left: 95px; top: 1146px;
    color: var(--white); font-size: 12.5px;
  }
</style>
</head>
<body>
<div class="page">
  <header>
    <div class="brand">
      <span class="brand-mark"></span>
      <div class="brand-name">Bright Sprouts</div>
    </div>
    <div class="hero" role="img" aria-label="Mother smiling as her baby plays with a stacking toy"></div>
    <nav class="main-nav">
      <a href="#">Home</a>
      <a href="#">Our Method</a>
      <a href="#" class="is-current">The Program</a>
      <a href="#">Media</a>
      <a href="#">Locations</a>
      <a href="#">About Us</a>
      <a href="#">Contact Us</a>
      <a href="#">News &amp; Events</a>
    </nav>
  </header>

  <aside>
    <div class="cta cta-register">Register your<br>interest today!</div>
    <div class="cta cta-contact">
      Contact us!<br>T. +971 550 123 456
      <div class="social">
        <span role="img" aria-label="Social page link"></span>
        <span role="img" aria-label="Social feed link"></span>
      </div>
    </div>
  </aside>

  <main class="content">
    <div class="content-body">
      <h1>The Program</h1>
      <p>Our preschool program and accelerated learning activities are for the early learner age group 6 months to 6 years old.</p>
      <p>We currently offer the program in English.</p>
      <p>Our classes are 50 minutes and we request a parent or carer to attend the class with the child. Consistency and repetition is crucial in developing sound 'bridges' between hemispheres of the brain and therefore we do have staff available to assist your child in the class if at times the parent or carer is unable to attend.</p>
      <strong>Our program will:</strong>
      <ul class="benefits">
        <li>Enhance sensorial and critical thinking skills</li>
        <li>Develop photographic memory and recall skills</li>
        <li>Conditions children to love learning, develops an enquiring mind and encourages exploration</li>
        <li>Develops confidence and strengthens the bonds between children and their carers</li>
        <li>Develops children who delight in using all five senses</li>
        <li>Fosters creativity, intuition and confidence</li>
        <li>Lays the foundations for early reading, writing and numeracy skills</li>
        <li>Develops high speed memorisation and calculation</li>
        <li>Promotes social interaction and develops your child's personalities and strength</li>
      </ul>
      <h2>The 2013-2014 term dates are as follows</h2>
      <div class="terms">
        <div><b>TERM 1</b>October 20th - December 19th</div>
        <div><b>TERM 2</b>January 5th - April 10th</div>
        <div><b>TERM 3</b>April 20th - June 26th</div>
      </div>
      <p class="pricing">Class costs 180 AED per session.<br>We offer a 5% sibling discount and a 5% referral fee upon enrolment.</p>
      <p>Please contact us for more information on our program and to learn more about our unique approach to child development and early childhood education.</p>
    </div>
    <div class="side-photo side-photo-abacus" role="img" aria-label="Toddler working with an abacus and number cards"></div>
    <div class="side-photo side-photo-play" role="img" aria-label="Young child pointing at a colourful picture board"></div>
  </main>

  <footer class="footer-note">© 2013 Bright Sprouts</footer>
</div>
</body>
</html>
```